Our New Website is Now Live!

New website launch, with ability to place orders and save quotes online. Our previous website was resource oriented – www.flumevalvekit.com – and new website will be up to date, more interactive, more modern and have all and more repair resources. Company colors are in logo below and throughout new website – https://staging.sluicefixcrew.com/. We have always offered free technical phone support and we now will have the ability to chat live on the website with our team for customer service, technical support and any issues.

Target Market(s)

blue collar, 40-60 year old blue collar workers. Message needs to be clear and most people that will see this flyer are not familiar with our old website

Requirements
Must have
• new website launch, repair help, technical assistance
Nice to have
• online chat, pictures from website of product

```html
<!DOCTYPE html>
<html lang="en">
<head>
<meta charset="utf-8">
<title>Our New Website Is Now Live – Harbor Flow Parts Company</title>
<link rel="stylesheet" href="https://fonts.googleapis.com/css2?family=Oswald:wght@500;600&family=Montserrat:wght@600&family=Open+Sans:ital,wght@0,700;1,600;1,700&family=Lato:wght@400&display=swap">
<style>
  :root {
    --brand-blue: #3a4fa3;
    --brand-red: #e3103f;
    --text-navy: #1e3a9c;
    --text-grey: #333333;
    --icon-dark: #1a1a1a;
    --paper: #ffffff;
    --photo-tone-a: #8d8c89;
    --photo-tone-b: #c9c5bd;
    --product-tone: #ecebe8;
  }
  * { margin: 0; padding: 0; box-sizing: border-box; }
  html, body { width: 902px; height: 1200px; overflow: hidden; background: var(--paper); }
  .flyer { position: relative; width: 902px; height: 1200px; background: var(--paper); overflow: hidden; }

  .brand { position: absolute; top: 46px; left: 0; width: 902px; display: flex; justify-content: center; align-items: center; gap: 14px; }
  .brand-mark { width: 30px; height: 30px; background: var(--brand-red); border-radius: 50%; }
  .brand-name { font-family: "Open Sans", sans-serif; font-weight: 700; font-size: 27px; color: var(--brand-blue); line-height: 1.1; }

  .headline { position: absolute; left: 0; width: 902px; text-align: center; line-height: 1; }
  .headline-top { top: 122px; font-family: "Oswald", sans-serif; font-weight: 500; font-size: 90px; color: var(--brand-blue); letter-spacing: 3.5px; }
  .headline-live { top: 218px; font-family: "Montserrat", sans-serif; font-weight: 600; font-size: 80px; color: var(--brand-red); letter-spacing: 4px; padding-right: 26px; }

  .art { position: absolute; inset: 0; }

  .intro { position: absolute; left: 50px; top: 757px; width: 435px; font-family: "Open Sans", sans-serif; font-style: italic; font-weight: 600; font-size: 20px; line-height: 25px; color: var(--text-navy); }
  .service { position: absolute; left: 50px; top: 847px; width: 395px; font-family: "Lato", sans-serif; font-size: 20.5px; line-height: 25.3px; color: var(--text-grey); }

  .call-label { position: absolute; left: 50px; top: 1019px; font-family: "Oswald", sans-serif; font-weight: 500; font-size: 26px; line-height: 1; color: var(--brand-red); }
  .call-number { position: absolute; left: 50px; top: 1076px; font-family: "Oswald", sans-serif; font-weight: 500; font-size: 47px; line-height: 1; color: var(--paper); }

  .feature { position: absolute; color: var(--paper); font-family: "Open Sans", sans-serif; }
  .feature-title { font-weight: 700; font-size: 20px; line-height: 24px; letter-spacing: 0.2px; }
  .feature-text { font-style: italic; font-weight: 700; font-size: 11.5px; line-height: 1.3; margin-top: 2px; }
  .f-order { left: 611px; top: 736px; }
  .f-repair { left: 577px; top: 816px; width: 300px; }
  .f-service { left: 534px; top: 907px; width: 330px; }
  .f-shipping { left: 505px; top: 998px; }
  .f-inventory { left: 465px; top: 1090px; }
</style>
</head>
<body>
<main class="flyer">
  <header class="brand">
    <span class="brand-mark"></span>
    <span class="brand-name">Harbor Flow Parts Company</span>
  </header>

  <h1 class="headline headline-top">OUR NEW WEBSITE IS</h1>
  <h2 class="headline headline-live">NOW LIVE!</h2>

  <svg class="art" width="902" height="1200" viewBox="0 0 902 1200">
    <defs>
      <linearGradient id="photoTone" x1="0" y1="0" x2="1" y2="1">
        <stop offset="0" stop-color="var(--photo-tone-b)"/>
        <stop offset="1" stop-color="var(--photo-tone-a)"/>
      </linearGradient>
      <linearGradient id="productTone" x1="0" y1="0" x2="0" y2="1">
        <stop offset="0" stop-color="#f3f2ef"/>
        <stop offset="1" stop-color="var(--product-tone)"/>
      </linearGradient>
    </defs>

    <polygon class="accent-stripe" points="540,325 902,325 902,342 523,342" fill="var(--brand-red)"/>

    <rect class="product-lineup" x="52" y="336" width="255" height="378" rx="6" fill="url(#productTone)" role="img" aria-label="Backflow test kits, a needle valve and a red gate valve"/>

    <polygon class="parts-photo" points="431,347 902,347 902,712 238,712" fill="url(#photoTone)" role="img" aria-label="Brass valve body, springs, check parts and a wrench laid out on concrete"/>

    <polygon class="feature-panel" points="585,712 902,712 902,1200 327,1200" fill="var(--brand-red)"/>

    <rect class="phone-band" x="0" y="1064" width="370" height="69" fill="var(--brand-blue)"/>

    <g class="feature-icons" stroke="var(--brand-red)" stroke-width="3" fill="var(--paper)">
      <circle cx="550" cy="755" r="45"/>
      <circle cx="511" cy="843" r="45"/>
      <circle cx="467" cy="931" r="45"/>
      <circle cx="431" cy="1022" r="45"/>
      <circle cx="394" cy="1115" r="45"/>
    </g>

    <g class="icon-mouse" transform="translate(550 755)" fill="#333">
      <rect x="-12" y="-30" width="24" height="34" rx="12"/>
      <line x1="0" y1="-30" x2="0" y2="-16" stroke="#fff" stroke-width="2"/>
      <text x="0" y="22" text-anchor="middle" font-family="Open Sans, sans-serif" font-weight="700" font-size="8">ORDER ONLINE!</text>
    </g>

    <g class="icon-repair" transform="translate(511 843)">
      <circle r="20" fill="none" stroke="#333" stroke-width="9" stroke-dasharray="6 4"/>
      <circle r="13" fill="#333"/>
      <circle r="6" fill="#fff"/>
      <line x1="-19" y1="21" x2="13" y2="-11" stroke="var(--brand-red)" stroke-width="7" stroke-linecap="round"/>
    </g>

    <g class="icon-support" transform="translate(467 931)" fill="none" stroke="var(--icon-dark)" stroke-width="4">
      <path d="M-20 2 a20 20 0 0 1 40 0"/>
      <rect x="-25" y="-1" width="9" height="15" rx="3" fill="var(--icon-dark)"/>
      <rect x="16" y="-1" width="9" height="15" rx="3" fill="var(--icon-dark)"/>
      <path d="M20 14 q0 12 -14 12"/>
      <path d="M-22 32 q22 -14 44 0" stroke-width="6"/>
    </g>

    <g class="icon-truck" transform="translate(431 1022)" fill="var(--icon-dark)">
      <rect x="-15" y="-11" width="30" height="22" rx="2"/>
      <path d="M16 -6 h10 l7 8 v9 h-17 z"/>
      <circle cx="-7" cy="14" r="4"/>
      <circle cx="23" cy="14" r="4"/>
      <g stroke="var(--icon-dark)" stroke-width="2"><line x1="-29" y1="-6" x2="-19" y2="-6"/><line x1="-27" y1="1" x2="-19" y2="1"/><line x1="-25" y1="8" x2="-19" y2="8"/></g>
      <text x="0" y="4" text-anchor="middle" fill="#fff" font-family="Open Sans, sans-serif" font-style="italic" font-weight="700" font-size="9">FAST</text>
    </g>

    <g class="icon-warehouse" transform="translate(394 1115)" fill="var(--icon-dark)">
      <path d="M-22 -5 l22 -13 l22 13 v25 h-44 z"/>
      <rect x="-14" y="-1" width="28" height="19" fill="#fff"/>
      <g stroke="var(--icon-dark)" stroke-width="2"><line x1="-14" y1="4" x2="14" y2="4"/><line x1="-14" y1="9" x2="14" y2="9"/><line x1="-14" y1="14" x2="14" y2="14"/></g>
    </g>
  </svg>

  <p class="intro">We are nation's leading source for genuine OEM backflow repair parts, repair information and technical assistance.</p>
  <p class="service">We have the best customer service in the industry. We pride ourselves in being knowledgeable, courteous, and caring. Meet the people who take care of you.</p>

  <p class="call-label">NEED HELP QUICK? JUST CALL:</p>
  <p class="call-number">(800) 555-0142</p>

  <section class="feature f-order"><h3 class="feature-title">ORDER ONLINE</h3><p class="feature-text">Process orders and save quotes</p></section>
  <section class="feature f-repair"><h3 class="feature-title">REPAIR RESOURCES</h3><p class="feature-text">Free Technical Phone Support, Step by Step Repair Instructions and Videos and Live Online Chat</p></section>
  <section class="feature f-service"><h3 class="feature-title">CUSTOMER SERVICE</h3><p class="feature-text">Friendly staff, troubleshooting solutions and steadfast dependability</p></section>
  <section class="feature f-shipping"><h3 class="feature-title">FAST SHIPPING</h3><p class="feature-text">1-2 day delivery anywhere in the US</p></section>
  <section class="feature f-inventory"><h3 class="feature-title">WORLD CLASS INVENTORY</h3><p class="feature-text">Widest range of manufacturer parts, tools and accessories</p></section>
</main>
</body>
</html>
```